Wine label - premium, elegant & classic

We are a young husband and wife team who have worked in the wine industry for 10+ years. This year we've finally had the opportunity to make our own wine and release our own brand. Our wines are boutique and sell at a mid-premium price (we don't make a lot) so we're looking for a label design that can reflect this premium nature and mixes traditional design elements with modern reflections.

The brand is called: M&L
Updates

Project Deadline Extended
Reason: We've received some great design concepts over the past week which we would happily pay for, so we've decided to guarantee payment and extend the deadline to allow time for more designs to be sent through. A BIG thanks to all who have already submitted, your designs are still under consideration. Cheers, L.

A big thank you to all for taking the time to submit your beautiful designs to our project.  We now have the very tough job of looking over each of them and selecting only one.  We hope to come to a decision in the next day or two, so hopefully we won't keep you waiting too long!

Cheers, and thanks again

M&L.                                   

Target Market(s)

30 - 45 year old female and male wine drinkers

Industry/Entity Type

Industry

Requirements
Must have
• Can we please see two versions of the one design - one for a red wine and one for a white wine.

The front labels needs to include the following information:
1. Brand name: M&L
2. Wine varieties: Pinot Noir (red wine) and Sauvignon Blanc (white wine)
3. Vintage: 2012 for both
4. Region: Yarra Valley
5. GI: Wine of Australia (not essential to be on front label)

The back label needs to include the following:
1. The brand name: M&L
2. Variety, vintage, region and volume (the volume must be 4mm in height)
3. Room for product description - approx. 30-40 words.
4. Alcohol statement (no size restriction, pls use 12.5% ALC/VOL as example)
5. Standard drinks (no size restriction, pls use 'Approx.7.8 standard drinks' as example)
6. Sulphites statement: "Sulphites added."
7. Allergen statement: "Fined with the aid of egg and milk products and traces may remain."
8. Room for address: Approx. 20 words
9. "Wine of Australia" - no size restriction, just needs to be legible

Packaging presentation:
Pinot Noir is a red wine and Sauvignon Blanc is a white wine.
Labels for both need to be shown on premium punted burgundy bottles (pls see example: http://www.pelvornglass.com/products_services/pvg_premium_burgundy_750_ml_wine_bottle.html)
Nice to have
• We would like the design to embody the following elements:
1. Classically modern
2. Clean and simple
3. Elegance
4. Restricted use of colours (ideally just black/grey, white/buff and perhaps one other)

Some design examples of what we like:
1. http://www.fenwickhollow.com.au/sangiovese-tasting-notes/
2. http://corlunbend.com/Wines/Corlun-Bend-Vineyard/Range/2010-Corlun-Bend-Single-Vineyard-Pinot-Noir-.htm
Should not have
• Preferrably won't have any photos or drawings unless you feel there is a simple symbol or image that could be used to enhance the design.

Restricted use of colours - more muted, conservative tones.

```html
<!DOCTYPE html>
<html lang="en">
<head>
<meta charset="utf-8">
<title>M&amp;L Sauvignon Blanc Label</title>
<link rel="stylesheet" href="https://fonts.googleapis.com/css2?family=Libre+Baskerville:wght@700&family=Playfair+Display:wght@400&display=swap">
<style>
  :root {
    --backdrop-centre: #fdfcfa;
    --backdrop-edge: #e4d6c1;
    --label-buff: #e2d3bc;
    --label-inner: #e6d8c3;
    --label-tab: #d8c7ad;
    --label-white: #ffffff;
  }
  html, body {
    margin: 0;
    padding: 0;
    width: 1200px;
    height: 960px;
    overflow: hidden;
  }
  .canvas {
    position: relative;
    width: 1200px;
    height: 960px;
    background: radial-gradient(ellipse at center, var(--backdrop-centre) 0%, var(--backdrop-centre) 45%, var(--backdrop-edge) 100%);
  }
  .front-label {
    position: absolute;
    left: 300px;
    top: 180px;
    width: 600px;
    height: 600px;
  }
  .label-serif {
    font-family: "Libre Baskerville", "Times New Roman", serif;
    font-weight: 700;
    fill: var(--label-white);
  }
  .vintage { font-size: 26px; letter-spacing: 1px; }
  .region { font-size: 11px; }
  .gi-line { font-size: 10px; }
  .variety { font-size: 32px; }
  .brand-name {
    font-family: "Playfair Display", Georgia, serif;
    font-weight: 400;
    font-size: 82px;
    fill: var(--label-white);
  }
</style>
</head>
<body>
<main class="canvas">
  <svg class="front-label" viewBox="0 0 500 500" role="img" aria-label="M&amp;L 2012 Yarra Valley Sauvignon Blanc, Wine of Australia">
    <defs>
      <path id="variety-arc" d="M 58 250 A 192 192 0 0 0 442 250"/>
    </defs>

    <circle class="label-disc" cx="250" cy="250" r="205" fill="var(--label-buff)"/>

    <path class="region-tab" d="M 125.9 145.9 A 162 162 0 0 1 331 109.7" fill="none" stroke="var(--label-tab)" stroke-width="18"/>
    <path class="ring-band ring-band--left" d="M 125.9 145.9 A 162 162 0 0 0 109.7 331" fill="none" stroke="var(--label-white)" stroke-width="12"/>
    <path class="ring-band ring-band--right" d="M 331 109.7 A 162 162 0 0 1 402.2 305.4" fill="none" stroke="var(--label-white)" stroke-width="12"/>

    <circle class="inner-ring" cx="250" cy="250" r="140" fill="none" stroke="var(--label-white)" stroke-width="1.5"/>
    <circle class="inner-disc" cx="250" cy="250" r="128" fill="var(--label-inner)" stroke="var(--label-white)" stroke-width="2.5"/>

    <text class="label-serif vintage" x="250" y="71" text-anchor="middle">2012</text>
    <text class="label-serif region" x="250" y="92" text-anchor="middle">Yarra Valley</text>

    <text class="brand-name" x="250" y="278" text-anchor="middle">M&amp;L</text>

    <text class="label-serif gi-line" x="250" y="404" text-anchor="middle">Wine of Australia</text>

    <text class="label-serif variety">
      <textPath href="#variety-arc" startOffset="50%" text-anchor="middle">Sauvignon Blanc</textPath>
    </text>
  </svg>
</main>
</body>
</html>
```